Taboun Dinner, Dessert and Drinks Menu

We need to redesign our Dinner, Desserts, and Drinks Menus.
I have attached all three menus as pdfs. I have chosen the higher payment option because its a few pages and have removed the refund option
Taboun is the most popular Lebanese Restaurant in Melbourne and is a combination of Great Quality Traditional Food and a clean warm ambiance.
Updates
The main part of the menu is the Banquets Section. We want to push our Banquets.
The main focus of the drinks is Lebanese Wines, Lebanese Beer, Lebanese Drinks. Anything Traditional
For the Coffee Menu,
We will be Adding a Chai Latte, More Flavoured Loose Leaf Teas and Removing the Stick Tea. We will also be adding 4 coffee flavour shots to our menu.
Industry/Entity Type
Restaurant
Look and feel
Each slider illustrates characteristics of the customer's brand and the style your logo design should communicate.

```html
<!DOCTYPE html>
<html lang="en">
<head>
<meta charset="utf-8">
<title>Taboun Desserts Menu</title>
<link href="https://fonts.googleapis.com/css2?family=Stint+Ultra+Condensed&family=Mulish:ital,wght@0,700;0,800;1,400;1,700&display=swap" rel="stylesheet">
<style>
:root{
  --lime:#cfdc68;
  --lime-soft:#e7ecb8;
  --price:#b3c64a;
  --ink:#111;
  --body:#222;
  --red:#e02020;
  --paper:#fff;
  --frame:#c9d862;
}
*{margin:0;padding:0;box-sizing:border-box}
html,body{width:848px;height:1200px;overflow:hidden;background:var(--paper)}
.menu{position:relative;width:848px;height:1200px;overflow:hidden;font-family:"Mulish",Arial,sans-serif;color:var(--body)}
.abs{position:absolute}
.top-band{left:0;top:0;width:848px;height:8px;background:var(--lime)}
.title,.dish,.section-title{font-family:"Stint Ultra Condensed",Georgia,serif;color:var(--ink);line-height:1;white-space:nowrap;font-weight:400;transform-origin:left top;-webkit-text-stroke:0.9px var(--ink)}
.title{left:35px;top:30px;font-size:90px;transform:scaleX(0.76)}
.section-title{left:35px;top:640px;font-size:100px;transform:scaleX(0.75);-webkit-text-stroke:1.2px var(--ink)}
.dish{font-size:56px;transform:scaleX(0.93)}
.dish.tight{transform:scaleX(0.87)}
.dish small{font-family:"Mulish",Arial,sans-serif;font-size:13px;font-weight:800;margin-left:8px;vertical-align:middle;-webkit-text-stroke:0}
.brand-box{left:553px;top:35px;width:192px;height:82px;display:flex;align-items:center;justify-content:center}
.brand{font-family:"Stint Ultra Condensed",Georgia,serif;font-size:60px;line-height:1;color:var(--ink)}
.price{font-weight:800;font-size:14px;color:var(--price);white-space:nowrap}
.price.dark{color:var(--ink)}
.favourite{font-weight:800;font-size:12px;color:var(--red)}
.desc{font-style:italic;font-size:12.6px;line-height:1.2;color:var(--body);width:445px}
.highlight{left:19px;width:501px;background:var(--lime-soft)}
.photo{border:5px solid var(--frame)}
.photo-label{background:var(--lime-soft);font-weight:800;font-size:11.5px;color:var(--ink);padding:2px 8px}
.list{font-style:italic;font-size:12.6px;line-height:1.2;color:var(--body);display:grid;grid-template-columns:140px 160px}
.footer{left:0;top:1147px;width:848px;height:53px;background:var(--lime);display:flex;align-items:center;justify-content:center;text-align:center;font-weight:700;font-style:italic;font-size:13.4px;line-height:1.3;color:var(--ink)}
</style>
</head>
<body>
<main class="menu">
  <div class="abs top-band"></div>
  <h1 class="abs title">TABOUN DESSERTS MENU</h1>
  <div class="abs brand-box"><span class="brand">Taboun</span></div>

  <div class="abs photo" style="left:554px;top:130px;width:293px;height:151px;background:var(--frame)"></div>
  <div class="abs" role="img" aria-label="Layali Libnan pudding in a bowl topped with pistachios" style="left:559px;top:135px;width:138px;height:141px;background:radial-gradient(circle at 50% 55%,#f4f1e6 0,#d9d6c8 45%,#3c4035 100%)"></div>
  <div class="abs" role="img" aria-label="Square of Namoura semolina cake with an almond" style="left:700px;top:135px;width:142px;height:141px;background:radial-gradient(circle at 50% 50%,#c88a4a 0,#e9c9a3 40%,#fafafa 75%)"></div>
  <div class="abs photo-label" style="left:566px;top:246px">Layali Libnan</div>
  <div class="abs photo-label" style="left:712px;top:246px">Namoura</div>

  <div class="abs" role="img" aria-label="Stacked pieces of baklawa topped with crushed pistachio" style="left:533px;top:281px;width:315px;height:440px;background:radial-gradient(ellipse at 65% 55%,#c9a36a 0,#b98c55 35%,#e3d2b4 62%,rgba(255,255,255,0) 80%)"></div>
  <div class="abs photo-label" style="left:449px;top:697px">Baklawa</div>

  <div class="abs photo" role="img" aria-label="Lebanese coffee served on a brass tray with a cup and water glass" style="left:592px;top:731px;width:254px;height:203px;background:radial-gradient(ellipse at 45% 50%,#d8c07a 0,#a88840 45%,#5a4a2e 100%)"></div>
  <div class="abs photo-label" style="left:644px;top:896px">Lebanese Coffee</div>

  <h2 class="abs dish" style="left:35px;top:136px">Baklawa</h2>
  <div class="abs price" style="left:373px;top:166px">$5.90 (3 Pieces)</div>
  <p class="abs desc" style="left:35px;top:196px">A Middle Eastern delicacy. Baked layers of very thin filo pastry stuffed with chopped cashews and topped with homemade rose syrup.</p>

  <h2 class="abs dish" style="left:35px;top:229px">Namoura</h2>
  <div class="abs price" style="left:373px;top:262px">$5.90 (3 Pieces)</div>
  <p class="abs desc" style="left:35px;top:289px">Lebanese semolina cake topped with almonds and homemade syrup.</p>

  <div class="abs highlight" style="top:331px;height:90px"></div>
  <h2 class="abs dish" style="left:35px;top:334px">Layali Libnan<small>(Lebanese Nights)</small></h2>
  <div class="abs price dark" style="left:375px;top:361px">$6.90</div>
  <p class="abs desc" style="left:35px;top:390px">This is a cold semolina pudding with real home distilled rosewater, topped with hand crushed pistachios, homemade cream and syrup.</p>

  <h2 class="abs dish" style="left:35px;top:432px">Rahat al Halkoum</h2>
  <div class="abs price" style="left:373px;top:464px">$5.90 (3 Pieces)</div>
  <p class="abs desc" style="left:35px;top:489px">Lebanese Turkish Delights that are flavoured with rosewater or lemon and served in between traditional round Karami biscuits.</p>

  <h2 class="abs dish" style="left:35px;top:532px">Halawet al Jebn</h2>
  <div class="abs favourite" style="left:376px;top:545px">TABOUN FAVOURITE</div>
  <div class="abs price" style="left:376px;top:561px">$6.90</div>
  <p class="abs desc" style="left:35px;top:590px">A popular Lebanese dessert made from sweet cheese which is drizzled with homemade rosewater syrup then topped with crushed pistachio.</p>

  <h2 class="abs section-title">COFFEES &amp; TEAS</h2>

  <div class="abs highlight" style="top:731px;height:114px"></div>
  <h2 class="abs dish" style="left:35px;top:735px">Café Blanc</h2>
  <div class="abs price dark" style="left:373px;top:766px">$6.90</div>
  <p class="abs desc" style="left:35px;top:793px">Café Blanc is a sedative that calms the nerves while stimulating digestion after a particularly rich or heavy meal. Café Blanc is a soothing combination of hot water and Orange Blossom water.</p>

  <h2 class="abs dish tight" style="left:35px;top:862px">Lebanese Coffee Tray</h2>
  <div class="abs price" style="left:360px;top:892px">$3.50</div>

  <h2 class="abs dish" style="left:35px;top:937px">Other Available Coffees</h2>
  <div class="abs price" style="left:360px;top:969px">$3.50</div>
  <div class="abs list" style="left:35px;top:998px">
    <span>Cappuccino</span><span>Long Macchiato</span>
    <span>Café Latte</span><span>Short Black</span>
    <span>Chai Latte</span><span>Long Black</span>
    <span>Short Macchiato</span><span>Flat White</span>
  </div>

  <h2 class="abs dish" style="left:35px;top:1077px">Hot Chocolate</h2>
  <div class="abs price" style="left:360px;top:1108px">$4.50</div>

  <h2 class="abs dish" style="left:443px;top:937px">Traditional Teas</h2>
  <div class="abs price" style="left:769px;top:969px">$3.50</div>
  <div class="abs list" style="left:443px;top:1000px;grid-template-columns:202px 160px">
    <span>Lebanese Loose Leaf Tea</span><span>Lebanese Anise Tea</span>
    <span>Lebanese Mint Tea</span><span>Lebanese Mountain Tea</span>
  </div>

  <h2 class="abs dish" style="left:443px;top:1045px">Coffee Flavoured Shots</h2>
  <div class="abs price" style="left:769px;top:1076px">$3.50</div>
  <div class="abs list" style="left:443px;top:1105px;grid-template-columns:202px 160px">
    <span>Flavour X</span><span>Flavour X</span>
    <span>Flavour X</span><span>Flavour X</span>
  </div>

  <footer class="abs footer">Please note, a 2% credit card surcharge will apply to all credit card transactions<br>(including where you select the 'credit' option when paying by debit card).</footer>
</main>
</body>
</html>
```